Email signature

I have an email signature, card and letter head and I would like the colours darker and more distinctive and I would like the contact details to be bigger and or easier to read as they are hard to read at the moment. The arrow watermark is fine I think.

Logo Text

CORVELL GUARD PTY LTD

Requirements
Nice to have
• The yellow type colour with the grey is good and I would like to retain that, but it looks washed out and too light on the screen. I like the arrows and I like the watermark arrows as well and I would like to retain the basic design.

```html
<!DOCTYPE html>
<html lang="en">
<head>
<meta charset="utf-8">
<title>Corvell Guard Letterhead</title>
<link rel="stylesheet" href="https://fonts.googleapis.com/css2?family=Roboto:wght@300;400&display=swap">
<style>
  :root {
    --backdrop: #ececed;
    --paper: #ffffff;
    --brand-yellow: #e8970a;
    --brand-grey: #4a4b4d;
    --text-grey: #3f4042;
    --watermark-tone: #f0f1f1;
  }
  html, body {
    margin: 0;
    padding: 0;
    width: 1200px;
    height: 1000px;
    overflow: hidden;
    background: var(--backdrop);
    font-family: "Roboto", Arial, sans-serif;
  }
  .letterhead {
    position: absolute;
    left: 278px;
    top: 45px;
    width: 644px;
    height: 910px;
    background: var(--paper);
  }
  .watermark {
    position: absolute;
    left: 0;
    top: 150px;
    width: 497px;
    height: 216px;
    background: linear-gradient(90deg, var(--watermark-tone) 0%, var(--watermark-tone) 70%, rgba(240,241,241,0) 100%);
  }
  .brand {
    position: absolute;
    right: 34px;
    top: 56px;
    text-align: right;
    color: var(--brand-grey);
    font-weight: 300;
  }
  .brand-name {
    display: flex;
    align-items: center;
    justify-content: flex-end;
    gap: 12px;
    font-size: 36px;
    line-height: 40px;
    letter-spacing: 0.5px;
  }
  .brand-mark {
    width: 14px;
    height: 14px;
    background: var(--brand-yellow);
  }
  .brand-suffix {
    display: block;
    font-size: 21px;
    line-height: 24px;
    letter-spacing: 2px;
    margin-top: 2px;
  }
  .contact {
    position: absolute;
    left: 0;
    right: 0;
    bottom: 34px;
    text-align: center;
    color: var(--text-grey);
    font-size: 13.5px;
    font-weight: 400;
    line-height: 22px;
    white-space: nowrap;
  }
  .contact-line { margin: 0; }
  .contact-item { margin: 0 5px; }
  .contact-label { color: var(--brand-yellow); }
</style>
</head>
<body>
  <main class="letterhead">
    <div class="watermark" role="img" aria-label="Faint watermark band of repeated chevron arrows"></div>

    <header class="brand">
      <div class="brand-name"><span class="brand-mark"></span><span>CORVELL GUARD</span></div>
      <span class="brand-suffix">PTY LTD</span>
    </header>

    <footer class="contact">
      <p class="contact-line">214 Tallowood Road, Kelso NSW 2795</p>
      <p class="contact-line">
        <span class="contact-item"><span class="contact-label">ABN:</span> 52 317 604 219</span>
        <span class="contact-item">PH: 0428 561 903</span>
        <span class="contact-item"><span class="contact-label">E:</span> dan@corvellguard.net.au</span>
        <span class="contact-item"><span class="contact-label">W:</span> www.corvellguard.net.au</span>
      </p>
    </footer>
  </main>
</body>
</html>
```